need corporate, modern business card created for Consulting Company

I need a slick business card using elements from my website, as well as, integrating my pixelharbor-created logo (see files).

The business card needs to be:
1. Corporate and modern
2. Clean and professional

I've included a PSD with the logo/icon that you can use to create it. Feel free to try a metallic finish on the logo, make it bigger/small, underlay it. Whatever you need to do to make my card stand out.

Try a black background, or white background or gray.

The idea is for my card to be memorable as well as professional and corporate.

Target Market(s)

Corporate business in the US and Canada.

Industry/Entity Type

Business

Contact Information for Business Card

Business Leveraging Technology
Malcolm Tudd, Senior Partner
office: 1 877 555 0143
mobile: 1 519 555 0172
website: http://www.vextorial.com

Requirements
Must have
• Card-related information
• corporate, yet modern
• clean and professional
• incorporate the icon only
• must have an editable form when complete!
Nice to have
• metallic icon might be cool
• try it with white or black

```html
<!DOCTYPE html>
<html lang="en">
<head>
<meta charset="utf-8">
<title>Vextorial Business Card</title>
<link rel="stylesheet" href="https://fonts.googleapis.com/css2?family=Open+Sans:wght@300;400;700&display=swap">
<style>
  :root {
    --stage: #b4bac2;
    --card-black: #1f1f20;
    --brand-blue: #2f6bbf;
    --swoosh-grey: #a7a8ac;
    --text-white: #ffffff;
  }
  * { margin: 0; padding: 0; box-sizing: border-box; }
  html, body {
    width: 1200px;
    height: 866px;
    overflow: hidden;
  }
  body {
    background: var(--stage);
    font-family: "Open Sans", Arial, sans-serif;
    position: relative;
  }
  .card {
    position: absolute;
    top: 278px;
    width: 540px;
    height: 310px;
    background: var(--card-black);
    overflow: hidden;
    box-shadow: 0 10px 28px rgba(0,0,0,0.22);
  }
  .card--back { left: 40px; }
  .card--front { left: 620px; }

  .brand-name {
    display: flex;
    align-items: center;
    gap: 10px;
    color: var(--brand-blue);
    font-weight: 700;
    letter-spacing: -0.5px;
  }
  .brand-name__mark {
    width: 0.55em;
    height: 0.55em;
    background: var(--brand-blue);
  }
  .card--back .brand-name {
    position: absolute;
    left: 0; right: 0; top: 0; bottom: 0;
    justify-content: center;
    font-size: 62px;
  }

  .front-art {
    position: absolute;
    inset: 0;
    width: 540px;
    height: 310px;
  }
  .card--front .brand-name {
    position: absolute;
    left: 34px;
    top: 118px;
    font-size: 44px;
  }
  .holder {
    position: absolute;
    left: 34px;
    top: 196px;
    color: var(--text-white);
  }
  .holder__name { font-weight: 700; font-size: 17px; line-height: 1.2; }
  .holder__role { font-weight: 300; font-size: 16px; line-height: 1.25; }

  .contact {
    position: absolute;
    right: 22px;
    top: 96px;
    list-style: none;
    text-align: right;
    color: var(--text-white);
    font-size: 11.5px;
    line-height: 1.45;
  }
  .contact li { display: flex; justify-content: flex-end; align-items: center; gap: 5px; }
  .contact svg { width: 10px; height: 10px; fill: var(--text-white); }
</style>
</head>
<body>

<section class="card card--back" aria-label="Card back">
  <div class="brand-name"><span class="brand-name__mark"></span>vextorial</div>
</section>

<section class="card card--front" aria-label="Card front">
  <svg class="front-art" viewBox="0 0 540 310" aria-hidden="true">
    <path fill="var(--brand-blue)" d="M540 0 L540 310 L0 310 L0 290 C210 300 345 240 395 150 C430 80 460 30 510 0 Z"/>
    <path fill="var(--swoosh-grey)" d="M492 10 C440 45 410 110 378 160 C325 242 205 272 0 262 L0 276 C215 288 350 252 398 162 C428 104 455 45 492 10 Z"/>
    <path fill="var(--swoosh-grey)" d="M475 22 C425 72 398 160 338 200 C290 230 235 240 180 236 C255 226 305 200 345 150 C385 100 425 52 475 22 Z"/>
  </svg>

  <div class="brand-name"><span class="brand-name__mark"></span>vextorial</div>

  <div class="holder">
    <p class="holder__name">Dorian Pell-Avery</p>
    <p class="holder__role">Consultant</p>
  </div>

  <ul class="contact">
    <li>041.12th floor,Quay</li>
    <li>Linden Road KPR</li>
    <li>012 555 0147
      <svg viewBox="0 0 10 10"><path d="M2 0.5 L3.8 2.6 L2.8 3.8 C3.5 5.2 4.8 6.5 6.2 7.2 L7.4 6.2 L9.5 8 L8.3 9.5 C4.5 9.2 0.8 5.5 0.5 1.7 Z"/></svg>
    </li>
    <li>012 555 0147
      <svg viewBox="0 0 10 10"><rect x="2" y="0.5" width="6" height="3"/><rect x="0.5" y="4" width="9" height="5.5"/></svg>
    </li>
    <li>hello@vextorial.com
      <svg viewBox="0 0 10 10"><rect x="0.5" y="2" width="9" height="6.5"/></svg>
    </li>
    <li>www.vextorial.com</li>
  </ul>
</section>

</body>
</html>
```